Book cover for a sci fi book called The Velvet Assembly

Dear Pixel Harbor team,

I would need a book cover design for my sci fi book, 'The Velvet Assembly'.

I will start by briefing you about the book's content, then I would like to advice you about a few possible book cover scenarios that I could imagine having for the book, and on which I would like to ask you to work on.

Book abstract:

The velvet assembly is a technically developed and spiritually evolved society from a distant galaxy.

Main location the actions take place: Planet Earth, globalized world, former Northern Germany, a new isolated high tech city at the sea, called Lees, inhabitants from everywhere, one government, one religion.
• Year: 2093
• The Velvet Assembly: solar system with 7 suns. The inhabitans of the velvet assembly have no physical body, only energetical bodies. Only when visiting Earth, they can incarnate at will.

The action starts on planet Earth, where a group of 4 people, two women and two males, who meet through different circumstances and decide to follow together a spiritual and philiosophical path towards self development and evolution. They meet an incarnated master from the velvet assembly who leads their path. At the end of the books, they reach a form of enlightment and transcende to The Velvet Assembly, they only come to know at the end the truth about the real origin of their master.

For the book cover, no matter what ideas you choose, please use max three predominant colors for that, red, yellow and orange. The book cover should inspire warmth.

Suggestions for the design:
- an abstract sun
- a cosmic view of the velvet assembly
- an abstractized design of a sacred geometry shape
- sun in the upper left corner, shining with visible rays on the whole surface of the book cover, a group of 4 people with the female old master sitting by their side in the lower right corner
- an out of the box Ufo, please choose for example an asymmetrical shape, definately not the usual flying sorcer, departing from the velvet assembly solar system, cosmic view from above
- PLEASE FEEL FREE TO BRAINSTROM ON YOUR OWN IDEAS BASED ON WHAT THE BOOK ABSTRACT INSPIRED YOU

For any questions, I am atbyour disposal.

I am looking forward to your design, thank you in advance for that.

Kind regards,
Mira

Target Market(s)

Sci Fi enthusiasts
Philosophers

Font styles to use
Serif

Colors
fbee3e
ffc214
faa54b
f37122
f04a50

Requirements
Must have
• For the book cover, no matter what ideas you choose, please use max three predominant colors for that, red, yellow and orange and/or any derived hues. The book cover should inspire warmth.
• Suggestions for the design:
• - an abstract sun
• - a cosmic view of the velvet assembly
• - an abstractized design of a sacred geometry shape
• - sun in the upper left corner, shining with visible rays on the whole surface of the book cover, a group of 4 people with the female old master sitting by their side in the lower right corner
• - an out of the box Ufo, please choose for example an asymmetrical shape, definately not the usual flying sorcer, departing from the velvet assembly solar system, cosmic view from above
• - PLEASE FEEL FREE TO BRAINSTROM ON YOUR OWN IDEAS BASED ON WHAT THE BOOK ABSTRACT INSPIRED YOU
Nice to have
• Minimalistic and modern design
Should not have
• dark or grey shades
• phtographs

```html
<!DOCTYPE html>
<html lang="en">
<head>
<meta charset="utf-8">
<title>The Velvet Assembly — Book Cover</title>
<link rel="stylesheet" href="https://fonts.googleapis.com/css2?family=Cinzel:wght@400;600&display=swap">
<style>
  :root {
    --backdrop: #dde5e9;
    --space-deep: #1c0f14;
    --planet-brown: #6b3a2a;
    --sun-gold: #ffc214;
    --sun-amber: #faa54b;
    --ember-orange: #f37122;
    --velvet-red: #5e1a1c;
    --haze-pink: #d9606a;
    --floor-rose: #8a3a3a;
    --title-ink: #e4e4f2;
  }
  * { margin: 0; padding: 0; box-sizing: border-box; }
  html, body {
    width: 1200px;
    height: 1200px;
    overflow: hidden;
    background: var(--backdrop);
  }
  .book-cover {
    position: absolute;
    left: 230px;
    top: 76px;
    width: 740px;
    height: 1048px;
    overflow: hidden;
    box-shadow: 0 18px 40px rgba(40, 50, 60, 0.25);
    font-family: "Cinzel", "Times New Roman", serif;
    color: var(--title-ink);
    text-align: center;
  }
  .cover-art {
    position: absolute;
    inset: 0;
    width: 100%;
    height: 100%;
  }
  .title-kicker {
    position: absolute;
    left: 0; right: 0;
    top: 456px;
    font-size: 42px;
    font-weight: 400;
    letter-spacing: 2px;
    line-height: 1;
  }
  .title-main {
    position: absolute;
    left: 0; right: 0;
    top: 530px;
    font-size: 92px;
    font-weight: 600;
    line-height: 124px;
    letter-spacing: -1px;
  }
  .title-main span { display: block; }
  .author-name {
    position: absolute;
    left: 0; right: 0;
    top: 940px;
    font-size: 44px;
    font-weight: 400;
    letter-spacing: 8px;
    line-height: 1;
  }
</style>
</head>
<body>
  <main class="book-cover">
    <svg class="cover-art" viewBox="0 0 740 1048" role="img"
         aria-label="Cosmic scene: a large glowing planet with a golden sunrise rim in the upper half, a lone figure standing in a bright doorway amid red mist below">
      <defs>
        <linearGradient id="sky" x1="0" y1="0" x2="0" y2="1">
          <stop offset="0" stop-color="var(--space-deep)"/>
          <stop offset="0.35" stop-color="#4a2218"/>
          <stop offset="0.6" stop-color="var(--velvet-red)"/>
          <stop offset="0.85" stop-color="var(--floor-rose)"/>
          <stop offset="1" stop-color="#6e2a2c"/>
        </linearGradient>
        <radialGradient id="planet" cx="0.35" cy="0.25" r="0.75">
          <stop offset="0" stop-color="#8a5a3c"/>
          <stop offset="0.7" stop-color="var(--planet-brown)"/>
          <stop offset="0.93" stop-color="var(--ember-orange)"/>
          <stop offset="1" stop-color="var(--sun-gold)"/>
        </radialGradient>
        <radialGradient id="flare" cx="0.5" cy="0.5" r="0.5">
          <stop offset="0" stop-color="#fff2b0" stop-opacity="0.9"/>
          <stop offset="0.3" stop-color="var(--sun-amber)" stop-opacity="0.6"/>
          <stop offset="1" stop-color="var(--ember-orange)" stop-opacity="0"/>
        </radialGradient>
        <radialGradient id="haze" cx="0.5" cy="0.5" r="0.5">
          <stop offset="0" stop-color="#ffd0d0" stop-opacity="0.9"/>
          <stop offset="0.35" stop-color="var(--haze-pink)" stop-opacity="0.6"/>
          <stop offset="1" stop-color="var(--haze-pink)" stop-opacity="0"/>
        </radialGradient>
      </defs>
      <rect width="740" height="1048" fill="url(#sky)"/>
      <circle cx="230" cy="60" r="520" fill="url(#planet)"/>
      <ellipse cx="390" cy="460" rx="220" ry="140" fill="url(#flare)"/>
      <ellipse cx="400" cy="860" rx="380" ry="200" fill="url(#haze)"/>
    </svg>

    <p class="title-kicker">THE</p>
    <h1 class="title-main"><span>VELVET</span><span>ASSEMBLY</span></h1>
    <p class="author-name">AUTHOR NAME</p>
  </main>
</body>
</html>
```